The Long Lantern of a Harbour Town: A Chronicle of Patience, Courage and Kinship

I require designs for the front cover, rear cover and spine for a printed book. The book is the personal account of a stroke survivor.

Dimensions requested by publisher:|

Front + rear covers = 130 x 195mm with 3-5mm bleed
Spine = c. 10mm

Target Market(s)

Worldwide

Font styles to use
Decorative
Script

Requirements
Must have
• The text for the back cover (and I have attached photos for the accompanying headshot):

"Mira Ostend had become a successful commercial lawyer in Tanzania with a professional career that spanned almost two decades. One week after celebrating her law firm’s 5th anniversary her life changed dramatically when at 4am one morning she suffered an ischaemic stroke.

After losing the use of the right side of her body and her ability to speak and swallow, Mira was forced to undergo a full system reboot. In this brutally honest account of her life before and after the stroke Mira describes her physical and mental battles, how she managed to accept the condition and deal with the accompanying feelings of shame.

Her story is one of rebirth, hope and ultimately transformation, offering practical advice for stroke survivors, their families and anyone embarking on a rehabilitation programme following serious illness."
Nice to have
• Modern but elegant feel. Something that signifies the metamorphosis of a butterfly, or transformation in general.

```html
<!DOCTYPE html>
<html lang="en">
<head>
<meta charset="utf-8">
<title>The Long Lantern of a Harbour Town – Cover Spread</title>
<link rel="stylesheet" href="https://fonts.googleapis.com/css2?family=Kaushan+Script&family=EB+Garamond:wght@400;600&family=Catamaran:wght@600&family=Cormorant+Garamond:wght@500&display=swap">
<style>
  :root {
    --plum: #5c1637;
    --plum-deep: #4e112e;
    --gold: #c9a86a;
    --paper: #ffffff;
    --backdrop: #f1f1f1;
    --ink-light: #f6eef2;
  }
  * { box-sizing: border-box; margin: 0; padding: 0; }
  html, body { width: 899px; height: 1200px; overflow: hidden; background: var(--backdrop); }
  .spread {
    position: absolute; left: 20px; top: 302px;
    width: 860px; height: 595px;
    display: flex;
    box-shadow: 0 2px 10px rgba(0,0,0,.12);
  }
  /* Back cover */
  .back-cover {
    position: relative; width: 397px; height: 100%;
    background: var(--plum); color: var(--ink-light);
  }
  .blurb {
    position: absolute; left: 36px; top: 39px; width: 316px;
    font-family: "EB Garamond", serif; font-size: 10.2px; line-height: 1.3;
    text-align: justify;
  }
  .blurb p + p { margin-top: 12px; }
  .author-bio {
    position: absolute; left: 36px; top: 253px; width: 316px;
    display: flex; gap: 8px;
  }
  .headshot {
    flex: none; width: 102px; height: 137px;
    background: linear-gradient(135deg, #d9463a 0%, #3f7fbf 45%, #e8c44a 100%);
  }
  .bio-text {
    font-family: "EB Garamond", serif; font-size: 9.3px; line-height: 1.25;
    text-align: justify; color: var(--ink-light);
  }
  .butterflies-photo {
    position: absolute; left: 0; bottom: 0; width: 178px; height: 200px;
    background: radial-gradient(ellipse at 40% 70%, rgba(214,136,52,.75) 0%, rgba(108,122,62,.55) 45%, rgba(92,22,55,0) 75%);
  }
  /* Spine */
  .spine {
    position: relative; width: 66px; height: 100%;
    background: var(--plum);
  }
  .spine-star { position: absolute; left: 24px; width: 18px; height: 18px; }
  .spine-star.top { top: 30px; }
  .spine-star.bottom { bottom: 26px; }
  .spine-text {
    position: absolute; left: 33px; top: 297px;
    transform: translate(-50%, -50%) rotate(-90deg);
    white-space: nowrap; display: flex; align-items: center; gap: 60px;
    color: var(--paper);
  }
  .spine-title { font-family: "Kaushan Script", cursive; font-size: 22px; }
  .spine-author { font-family: "Cormorant Garamond", serif; font-size: 10px; letter-spacing: 4px; }
  /* Front cover */
  .front-cover {
    position: relative; width: 397px; height: 100%;
    background: var(--paper); overflow: hidden;
  }
  .stem-photo {
    position: absolute; left: 250px; top: -20px; width: 7px; height: 520px;
    background: linear-gradient(#b9ab86, #a09070);
    transform: rotate(-14deg); transform-origin: top;
    border-radius: 3px; opacity: .8;
  }
  .chrysalis-photo {
    position: absolute; left: 197px; top: 328px; width: 106px; height: 204px;
    border-radius: 40% 40% 45% 45%;
    background: linear-gradient(170deg, #efe4e2 0%, #e08a2c 35%, #c2561a 70%, #2a1a14 100%);
  }
  .title {
    position: absolute; left: 18px; top: 30px; width: 362px;
    font-family: "Kaushan Script", cursive; color: var(--plum);
    text-align: center; line-height: 1;
  }
  .title span { display: block; }
  .title .t-small { font-size: 44px; }
  .title .t-large { font-size: 66px; margin-top: 2px; }
  .title .t-join { font-size: 32px; margin-top: 4px; }
  .title .t-wide { font-size: 54px; margin-top: 4px; }
  .subtitle-badge {
    position: absolute; left: 8px; top: 350px; width: 160px; height: 160px;
    border-radius: 50%; background: var(--plum);
    display: flex; flex-direction: column; align-items: center; justify-content: center;
    color: var(--paper); text-align: center;
    font-family: "Catamaran", sans-serif; font-weight: 600; font-size: 17px; line-height: 1.12;
  }
  .badge-stars { display: flex; gap: 3px; margin-top: 8px; }
  .badge-stars svg { width: 15px; height: 15px; }
  .author-name {
    position: absolute; left: 0; right: 0; top: 549px; text-align: center;
    font-family: "Cormorant Garamond", serif; font-size: 18px; letter-spacing: 8px;
    color: #1e1e1e;
  }
</style>
</head>
<body>
<main class="spread">
  <section class="back-cover">
    <div class="blurb">
      <p>Mira Ostend had become a successful commercial lawyer in Tanzania with a professional career that spanned almost two decades. One week after celebrating her law firm’s 5th anniversary her life changed dramatically when at 4am one morning she suffered an ischaemic stroke.</p>
      <p>After losing the use of the right side of her body and her ability to speak and swallow, Mira was forced to undergo a full system reboot. In this brutally honest account of her life before and after the stroke Mira describes her physical and mental battles, how she managed to accept the condition and deal with the accompanying feelings of shame.</p>
      <p>Her story is one of rebirth, hope and ultimately transformation, offering practical advice for stroke survivors, their families and anyone embarking on a rehabilitation programme following serious illness.</p>
    </div>
    <div class="author-bio">
      <div class="headshot" role="img" aria-label="Author headshot in front of a colourful mural"></div>
      <p class="bio-text">Mira Ostend lives by the sea with her family and a garden she tends slowly, one bed at a time. Before her stroke she spent almost twenty years in commercial law. Today she speaks to patient groups, mentors new survivors and writes about recovery, language and the quiet courage of ordinary days.</p>
    </div>
    <div class="butterflies-photo" role="img" aria-label="Two orange butterflies resting on thistle flowers"></div>
  </section>

  <section class="spine">
    <svg class="spine-star top" viewBox="0 0 24 24" aria-hidden="true"><polygon fill="var(--gold)" points="12,1 15,9 23,9 16.5,14 19,22 12,17 5,22 7.5,14 1,9 9,9"/></svg>
    <div class="spine-text">
      <span class="spine-title">The Long Lantern of a Harbour Town</span>
      <span class="spine-author">AUTHOR NAME</span>
    </div>
    <svg class="spine-star bottom" viewBox="0 0 24 24" aria-hidden="true"><polygon fill="var(--gold)" points="12,1 15,9 23,9 16.5,14 19,22 12,17 5,22 7.5,14 1,9 9,9"/></svg>
  </section>

  <section class="front-cover">
    <div class="stem-photo" role="img" aria-label="Slender plant stem crossing the cover"></div>
    <div class="chrysalis-photo" role="img" aria-label="Monarch butterfly emerging from its chrysalis on the stem"></div>
    <h1 class="title">
      <span class="t-small">The Long</span>
      <span class="t-large">Lantern</span>
      <span class="t-join">of a</span>
      <span class="t-wide">Harbour Town</span>
    </h1>
    <div class="subtitle-badge">
      <span>A Chronicle</span>
      <span>of Patience,</span>
      <span>Courage and</span>
      <span>Kinship</span>
      <div class="badge-stars" aria-hidden="true">
        <svg viewBox="0 0 24 24"><polygon fill="var(--gold)" points="12,1 15,9 23,9 16.5,14 19,22 12,17 5,22 7.5,14 1,9 9,9"/></svg>
        <svg viewBox="0 0 24 24"><polygon fill="var(--gold)" points="12,1 15,9 23,9 16.5,14 19,22 12,17 5,22 7.5,14 1,9 9,9"/></svg>
        <svg viewBox="0 0 24 24"><polygon fill="var(--gold)" points="12,1 15,9 23,9 16.5,14 19,22 12,17 5,22 7.5,14 1,9 9,9"/></svg>
      </div>
    </div>
    <p class="author-name">AUTHOR NAME</p>
  </section>
</main>
</body>
</html>
```